Book Cover - Goals

Create book cover for book
Title: Summit Drive
Subtitle: Push Past Your Limits, Find Strength Within Yourself

See the uploaded 1st version -- I want to see different concepts -- definitely want use white space and keep a blue color similiar if not the same as the one seen in that other version and see my notes/feedback.

:

Target Market(s)

Women + Men - 35-60
Self Help + Health

Industry/Entity Type

Health And Wellness

Font styles to use
Sans Serif

Colors
0692cd
34a7d7
85cae6
cee9f5

Requirements
Must have
• Picture of father and I that can be found here:(https://files.cloudvault-share.net/folders/7K9QxRm2_41PlVnwTbZuLeHsCq3)
• and I uploaded one too (I'd like to see it with our shirts on and off)
Nice to have
• Want it to be clean
• More gender neutral -- not overly masculine or femine
• I really like these book covers - so something similair woudl be great"
• Steady Steps: The 9-Week Meal Rhythm Method
• The Quiet Harvest Plan : Retune Your Habits for Gentle Fat Burning, Steady Vigor and Lasting Stamina
• Walk Far, Feel Light for Years

```html
<!DOCTYPE html>
<html lang="en">
<head>
<meta charset="utf-8">
<title>Summit Drive – Book Cover</title>
<link rel="stylesheet" href="https://fonts.googleapis.com/css2?family=Oswald:wght@500&family=Montserrat:wght@400;700&display=swap">
<style>
  :root {
    --stage: #88c3df;
    --paper: #ffffff;
    --paper-shade: #eef3f6;
    --brand-blue: #0692cd;
    --band-blue: #1590cc;
    --band-light: #34a7d7;
    --ink-light: #ffffff;
    --sub-ink: #d9eef8;
    --photo-warm: #d8a27e;
    --photo-cool: #4f78a8;
  }
  * { margin: 0; padding: 0; box-sizing: border-box; }
  html, body {
    width: 1200px;
    height: 1035px;
    overflow: hidden;
    background: var(--stage);
  }
  .canvas {
    position: relative;
    width: 1200px;
    height: 1035px;
    background: var(--stage);
  }
  .book-cover {
    position: absolute;
    left: 282px;
    top: 38px;
    width: 636px;
    height: 960px;
    background: linear-gradient(180deg, var(--paper) 0%, var(--paper) 55%, var(--paper-shade) 88%);
    overflow: hidden;
  }
  .author-photo {
    position: absolute;
    left: 134px;
    top: 78px;
    width: 372px;
    height: 690px;
    border-radius: 150px 150px 40px 40px;
    background: linear-gradient(180deg, var(--photo-warm) 0%, var(--photo-warm) 40%, var(--photo-cool) 58%, var(--photo-cool) 72%, var(--photo-warm) 80%, var(--photo-warm) 100%);
    opacity: 0.85;
  }
  .title {
    position: absolute;
    left: 0;
    width: 100%;
    text-align: center;
    font-family: "Oswald", sans-serif;
    font-weight: 500;
    color: var(--brand-blue);
    text-transform: uppercase;
    line-height: 1;
    opacity: 0.88;
  }
  .title-line-one {
    top: 262px;
    font-size: 168px;
    letter-spacing: 2px;
  }
  .title-line-two {
    top: 392px;
    font-size: 262px;
    letter-spacing: 2px;
  }
  .subtitle {
    position: absolute;
    left: 0;
    top: 792px;
    width: 100%;
    text-align: center;
    font-family: "Montserrat", sans-serif;
    font-weight: 400;
    font-size: 17px;
    line-height: 1.4;
    letter-spacing: 1px;
    color: var(--brand-blue);
  }
  .author-band {
    position: absolute;
    left: 0;
    bottom: 0;
    width: 100%;
    height: 118px;
    background: linear-gradient(180deg, var(--band-blue) 0%, var(--band-blue) 70%, var(--band-light) 100%);
    text-align: center;
    padding-top: 20px;
  }
  .author-names {
    font-family: "Montserrat", sans-serif;
    font-weight: 700;
    font-size: 32px;
    letter-spacing: 1px;
    color: var(--ink-light);
    text-transform: uppercase;
  }
  .author-tagline {
    margin-top: 4px;
    font-family: "Montserrat", sans-serif;
    font-weight: 400;
    font-size: 19px;
    letter-spacing: 2px;
    color: var(--sub-ink);
    text-transform: uppercase;
  }
</style>
</head>
<body>
  <main class="canvas">
    <article class="book-cover">
      <div class="author-photo" role="img" aria-label="Photo of the father and son authors standing back to back, shirtless, in board shorts"></div>
      <h1 class="title title-line-one">Summit</h1>
      <h1 class="title title-line-two">Drive</h1>
      <p class="subtitle">Push Past Your Limits,<br>Find Strength Within Yourself</p>
      <footer class="author-band">
        <p class="author-names">Dale &amp; Evan Marlow</p>
        <p class="author-tagline">The Father and Son Fitness Team</p>
      </footer>
    </article>
  </main>
</body>
</html>
```